IT Company that provides secure IT solutions and services to our customers

We need business cards and a logo for a new IT Solutions company just created based in Kuala Lumpur, Malaysia. But will also be serving other countries in the region. We provide secure data, voice solutions on mobile platforms. Our first offering is encrypted voice and data solutions for IOS, Android, Windows and BlackBerry devices.

Target Market(s)

large organizations Govt, Police, Defence, Anti-corruption, Legal, highly regulated industries such as Health-care, Financial, Banking, Insurance,

Industry/Entity Type

Information Technology

Contact Information for Business Card

VornaxIT (Logo - colour is ORBEL blue)Dariush Pelo Managing Director Vornax IT Sdn. Bhd.5th Floor, Block F, Wisma LBD,No.14 Jalan Seri Mewah,50470, Kuala LumpurMalaysia

Font styles to use
Sans Serif

Colors
3176b5
ec1f27
fbed22

Requirements
Must have
• VornaxIT all in Blue like ORBEL blue. A logo design perhaps a play of VI, K with a dangling T (colour can be any)
Nice to have
• I want a clean crisp card, not too busy, easy to read.

```html
<!DOCTYPE html>
<html lang="en">
<head>
<meta charset="utf-8">
<title>Vornax IT — Business Card</title>
<link href="https://fonts.googleapis.com/css2?family=Lato:wght@400;700;900&display=swap" rel="stylesheet">
<style>
  :root {
    --backdrop: #2a7fc4;
    --navy: #134f6b;
    --stripe: #1864a0;
    --mid-blue: #2a72b4;
    --light-blue: #3580bd;
    --rule: #2a6a90;
    --red: #ec1f27;
    --white: #ffffff;
    --muted: #b7c5d2;
  }
  * { margin: 0; padding: 0; box-sizing: border-box; }
  html, body { width: 1200px; height: 1000px; overflow: hidden; }
  body { background: var(--backdrop); font-family: "Lato", sans-serif; position: relative; }

  .card {
    position: absolute;
    width: 628px;
    height: 368px;
    overflow: hidden;
    box-shadow: 0 6px 16px rgba(0, 0, 0, 0.3);
  }
  .card__bg { position: absolute; inset: 0; width: 100%; height: 100%; }

  .card--front { left: 100px; top: 90px; }
  .card--back { left: 472px; top: 530px; }

  .wordmark {
    position: absolute;
    left: 0;
    right: 0;
    top: 188px;
    text-align: center;
    font-weight: 900;
    font-size: 66px;
    line-height: 1;
    color: var(--white);
    letter-spacing: -0.5px;
  }

  .holder__name {
    position: absolute;
    left: 53px;
    top: 72px;
    font-weight: 900;
    font-size: 31px;
    color: var(--white);
    letter-spacing: 0.3px;
  }
  .holder__title {
    position: absolute;
    left: 124px;
    top: 108px;
    font-size: 13px;
    color: var(--muted);
    letter-spacing: 0.4px;
  }

  .address {
    position: absolute;
    left: 213px;
    top: 284px;
    width: 200px;
    text-align: center;
    font-size: 9px;
    line-height: 12px;
    font-style: normal;
    color: var(--white);
  }
  .address__pin { position: absolute; left: 305px; top: 262px; width: 16px; height: 22px; }

  .mini-mark {
    position: absolute;
    left: 558px;
    top: 292px;
    font-weight: 900;
    font-size: 24px;
    line-height: 1;
    color: var(--white);
  }
</style>
</head>
<body>

  <section class="card card--front" aria-label="Card front">
    <svg class="card__bg" viewBox="0 0 628 368" aria-hidden="true">
      <rect width="628" height="368" fill="var(--mid-blue)"/>
      <polygon points="0,0 628,0 628,240 345,345 0,318" fill="var(--stripe)"/>
      <polygon points="0,0 628,0 628,222 345,326 0,300" fill="var(--navy)"/>
      <rect x="0" y="18" width="628" height="4" fill="var(--stripe)"/>
      <rect x="40" y="34" width="480" height="3" fill="var(--stripe)"/>
      <rect x="20" y="48" width="600" height="2" fill="var(--stripe)"/>
      <rect x="70" y="60" width="520" height="2" fill="var(--stripe)"/>
    </svg>
    <div class="wordmark">VornaxIT</div>
  </section>

  <section class="card card--back" aria-label="Card back">
    <svg class="card__bg" viewBox="0 0 628 368" aria-hidden="true">
      <rect width="628" height="368" fill="var(--light-blue)"/>
      <polygon points="0,0 512,0 600,184 512,368 0,368" fill="var(--mid-blue)"/>
      <polygon points="0,0 440,0 528,184 440,368 0,368" fill="var(--stripe)"/>
      <polygon points="0,0 415,0 502,184 415,368 0,368" fill="var(--navy)"/>
      <g stroke="var(--rule)" stroke-width="1.5">
        <line x1="0" y1="22" x2="420" y2="22"/>
        <line x1="44" y1="66" x2="295" y2="66"/>
        <line x1="104" y1="126" x2="355" y2="126"/>
        <line x1="44" y1="163" x2="295" y2="163"/>
        <line x1="219" y1="184" x2="470" y2="184"/>
        <line x1="0" y1="351" x2="420" y2="351"/>
      </g>
    </svg>

    <h1 class="holder__name">DARIUSH PELO</h1>
    <p class="holder__title">MANAGING DIRECTOR</p>

    <svg class="address__pin" viewBox="0 0 16 22" aria-hidden="true">
      <path d="M8 0C3.6 0 0 3.5 0 7.9 0 13.6 8 22 8 22s8-8.4 8-14.1C16 3.5 12.4 0 8 0z" fill="var(--red)"/>
      <circle cx="8" cy="8" r="3.2" fill="var(--navy)"/>
    </svg>
    <address class="address">
      Vornax IT Sdn.<br>
      Bhd.5th Floor, Block F<br>
      Wisma LBD<br>
      No.14 Jalan Seri Mewah, 50470<br>
      Kuala Lumpur, Malaysia
    </address>

    <div class="mini-mark">VI</div>
  </section>

</body>
</html>
```